New Web Page Design - Cement Rendering Business

Looking for a overhaul of our existing website (www.norpex.com.au).

Looking for a sleek and elegant design that incorporates the colours of our logos, black / green and white. Needs to look professional and want it to be well above what our competition is offering. (Findora search for 'cement rendering sydney' will display the competition we want to be well ahead of.

Prefer a mixture of pages with black background and white alternatively between home (black), about us (white), contact us (black) and gallery (white).

Would like to incorporate our logo on all pages attached preferably in the top left corner.

Website needs to be search engine optimised and have easily updated photo gallery which we already have.

Also need to embed our trackwise metrics code on the front home page.

Website needs to be able easily updated (text, pictures ) as required.
content management system should include fields where you can alter your page titles, meta description and keywords.

Pages also needs to be optimised for mobile devices, iphone, ipad and other mobile devices. (it is a current feature we have)

If you have any questions, just message me.

Please remember the look and feel of the site is important to us, we don't want it over complicated, simple elegant and professional in line with our logo standards.
Updates

Hi All, As an example of the look and feel we like. We have found a site that may assist in your design and creative process. http://demo.quorvix.org/ We like the simplicity, elegance and professional look of this site, although we would like it with our images, colours and logos. I hope this helps.! keep the great designs coming!

All, Thanks for the designs. Please try and use our website images due to copyright reasons for all your designs. Tomas

Target Market(s)

Construction Companies

Industry/Entity Type

Business

Colors
9bcb3b
acd036
474747

Requirements
Must have
• Search Engine Optimised.
Photo Gallery
Elegant/Professional Look & Feel.
Simple Yet Effective
Nice to have
• Moving Parts
Should not have
• Overly Complicated.
Cheap & Traditional Looking.
Boring

```html
<!DOCTYPE html>
<html lang="en">
<head>
<meta charset="utf-8">
<title>Norpex Cement Rendering</title>
<link href="https://fonts.googleapis.com/css2?family=Open+Sans:wght@300;400;600;700&family=Reenie+Beanie&display=swap" rel="stylesheet">
<style>
:root{
  --green:#9bcb3b;
  --green-bright:#acd036;
  --charcoal:#474747;
  --header:#1e1e1e;
  --hero:#2c2c2c;
  --footer:#2b2b2b;
  --footer-base:#1a1a1a;
  --light:#ececec;
  --text-grey:#8a8a8a;
  --white:#ffffff;
}
*{box-sizing:border-box;margin:0;padding:0}
html,body{width:759px;height:1200px;overflow:hidden;background:var(--white)}
body{position:relative;font-family:"Open Sans",Arial,sans-serif;color:var(--charcoal)}
.abs{position:absolute}

/* header */
.site-header{left:0;top:0;width:759px;height:50px;background:var(--header)}
.brand{left:26px;top:8px;display:flex;align-items:center;gap:10px}
.brand-dot{width:40px;height:40px;border-radius:50%;background:var(--green)}
.brand-name{font-size:24px;font-weight:700;color:var(--white);letter-spacing:1px}
.main-nav{right:28px;top:17px;display:flex;gap:16px;font-size:9px;font-weight:600;color:#cfcfcf;text-transform:uppercase}
.main-nav .active{color:var(--green)}
.main-nav .phone{color:var(--white);border-left:1px solid #555;padding-left:14px}

/* hero */
.hero{left:0;top:50px;width:759px;height:405px;background:radial-gradient(ellipse at 50% 30%,#3a3a3a 0%,var(--hero) 55%,#1e1e1e 100%)}
.hero-title{left:0;top:52px;width:759px;text-align:center;font-size:34px;font-weight:300;color:#cfd3c6}
.hero-title span{color:var(--green)}
.hero-sub{left:0;top:94px;width:759px;text-align:center;font-size:9px;color:#aaa}
.cta{left:310px;top:122px;width:138px;height:32px;background:var(--green);color:var(--white);font-size:14px;font-weight:600;text-align:center;line-height:32px;text-transform:uppercase;border-radius:2px}
.works-note{left:555px;top:118px;font-family:"Reenie Beanie",cursive;font-size:24px;color:#cfcfcf;transform:rotate(-8deg)}
.slide-side{top:200px;width:165px;height:150px;background:linear-gradient(135deg,#8d8a84,#5d5a55)}
.slide-left{left:42px}
.slide-right{left:552px;background:linear-gradient(135deg,#a8a49c,#6e6a63)}
.slide-shade{top:200px;width:165px;height:150px;background:rgba(0,0,0,.35)}
.slide-main{left:202px;top:157px;width:356px;height:224px;border:5px solid #f4f4f4;background:linear-gradient(120deg,#d9d6cf 0%,#bdb8ae 55%,#8f8a80 100%);box-shadow:0 8px 20px rgba(0,0,0,.6)}
.arrow{top:260px;width:18px;height:30px;background:rgba(255,255,255,.85)}
.arrow svg{display:block;margin:8px auto}

/* features */
.features{left:0;top:455px;width:759px;height:115px;background:var(--light)}
.feature{top:37px;display:flex;align-items:center;gap:10px;font-size:9px;color:#6a6a6a;line-height:1.5}
.feature svg{flex:none}

/* about band */
.about-band{left:0;top:595px;width:759px;height:340px;background:linear-gradient(110deg,#b79a7a 0%,#d8cbb9 35%,#9b8a78 70%,#6e6357 100%)}
.about-box{left:127px;top:720px;width:506px;height:130px;background:rgba(20,20,20,.82);color:var(--white);font-size:8.6px;line-height:1.45;text-align:center;padding:14px 26px}
.about-box p+p{margin-top:8px}

/* info bar */
.info-bar{left:0;top:955px;width:759px;height:46px;background:#f2f2f2;display:flex;justify-content:space-between;align-items:center;padding:0 60px;font-size:14px;font-weight:600;color:#9a9a9a}

/* footer */
.site-footer{left:0;top:1010px;width:759px;height:190px;background:var(--footer)}
.footer-col{top:28px;font-size:8.5px;color:#b5b5b5}
.footer-col h4{font-size:9.5px;font-weight:600;color:var(--white);text-transform:uppercase;margin-bottom:10px}
.footer-links li{list-style:none;padding:5px 0;border-bottom:1px solid #3d3d3d;width:120px}
.social li{list-style:none;display:flex;align-items:center;gap:8px;padding:4px 0}
.social i{display:block;width:14px;height:14px;border-radius:50%;background:#5a5a5a}
.map{left:360px;top:35px;width:112px;height:62px;background:linear-gradient(135deg,#e6e4dc,#cfd6c4)}
.contact p{line-height:1.55}
.footer-base{left:0;top:1178px;width:759px;height:22px;background:var(--footer-base);font-size:7.5px;color:#888;text-align:center;line-height:22px}
</style>
</head>
<body>

<header class="site-header abs">
  <div class="brand abs"><span class="brand-dot"></span><span class="brand-name">NORPEX</span></div>
  <nav class="main-nav abs">
    <span class="active">Home</span><span>About us</span><span>Contact us</span><span class="phone">548 207 3916</span>
  </nav>
</header>

<section class="hero abs">
  <h1 class="hero-title abs">Welcome to <span>Norpex</span></h1>
  <p class="hero-sub abs">Your one stop shop for all your cement rendering needs</p>
  <div class="cta abs">Contact us</div>
  <div class="works-note abs">Our works</div>

  <div class="slide-side slide-left abs" role="img" aria-label="Rendered wall project photo"></div>
  <div class="slide-shade abs" style="left:42px"></div>
  <div class="slide-side slide-right abs" role="img" aria-label="Rendered house exterior photo"></div>
  <div class="slide-shade abs" style="left:552px"></div>
  <div class="slide-main abs" role="img" aria-label="Freshly rendered cement wall corner photo"></div>
  <div class="arrow abs" style="left:207px"><svg width="8" height="14" viewBox="0 0 8 14"><path d="M7 1 1 7l6 6" fill="none" stroke="#444" stroke-width="2"/></svg></div>
  <div class="arrow abs" style="left:535px"><svg width="8" height="14" viewBox="0 0 8 14"><path d="M1 1l6 6-6 6" fill="none" stroke="#444" stroke-width="2"/></svg></div>
</section>

<section class="features abs">
  <div class="feature abs" style="left:120px">
    <svg width="32" height="32" viewBox="0 0 32 32"><circle cx="16" cy="16" r="14" fill="none" stroke="#9a9a9a" stroke-width="1.5"/><path d="M10 16.5l4 4 8-9" fill="none" stroke="#9a9a9a" stroke-width="2"/></svg>
    <div>25 years of experience<br>Fully trained</div>
  </div>
  <div class="feature abs" style="left:322px">
    <svg width="32" height="32" viewBox="0 0 32 32"><circle cx="16" cy="16" r="14" fill="none" stroke="#9a9a9a" stroke-width="1.5"/><path d="M10 16.5l4 4 8-9" fill="none" stroke="#9a9a9a" stroke-width="2"/></svg>
    <div>All work comes with warranty.<br>Work never outsourced</div>
  </div>
  <div class="feature abs" style="left:525px">
    <svg width="32" height="32" viewBox="0 0 32 32"><circle cx="16" cy="16" r="14" fill="none" stroke="#9a9a9a" stroke-width="1.5"/><path d="M10 16.5l4 4 8-9" fill="none" stroke="#9a9a9a" stroke-width="2"/></svg>
    <div>Fully licenced<br>Australian owned and operated</div>
  </div>
</section>

<section class="about-band abs" role="img" aria-label="Tradesman applying cement render to a wall"></section>
<div class="about-box abs">
  <p>We are an Australian owned and operated business with over 25 years of experience in our field. Our work is fully licensed, our employees are trained to the highest standards and all of our work is covered by warranty. We offer an obligation free on site consultation and quotation service for your convenience 7 days per week. We are the preferred supplier for many of the top building companies in Australia which gives you the access to our expertise, competitive rates and peace of mind.</p>
  <p>No job is too big or too small. We work on several residential, private and commercial projects all year round.</p>
</div>

<div class="info-bar abs">
  <span>Norpex Cement Rendering</span>
  <span>ABN: 418 602 377 15</span>
  <span>info@norpex.com.au</span>
</div>

<footer class="site-footer abs">
  <div class="footer-col abs" style="left:60px">
    <h4>Navigation link</h4>
    <ul class="footer-links"><li>Home</li><li>About Us</li><li>Contact Us</li></ul>
  </div>
  <div class="footer-col abs" style="left:235px">
    <h4>Follow us</h4>
    <ul class="social"><li><i></i>Friendly</li><li><i></i>Chirper</li><li><i></i>Findora+</li><li><i></i>RSS</li></ul>
  </div>
  <div class="map abs" role="img" aria-label="Location map"></div>
  <div class="footer-col contact abs" style="left:520px">
    <h4>Contact us</h4>
    <p>123, Street Number, Building Number,<br>Area Name, City Name, Zip Code</p>
    <p style="margin-top:8px">Call Us: 548 207 3916<br>Email: info@norpex.com.au</p>
  </div>
  <div class="footer-base abs" style="top:168px">©2014 Norpex | Terms of Service | Privacy Policy</div>
</footer>

</body>
</html>
```